Corporate Comedy Poster Brochure

I have designed an 10.75 by 15 flat one-sided poster/flyer to mail out for promoting my corporate comedy services. I don't think I did a bad job, but would love to see if someone can create something else for the same purpose, but with an expert hand and eye, as I am not a designer by trade. You should get a sense of it by the PSD example I provided.

FYI: My websites are:
www.paulvantrimm.com/corporate-comedian
www.gigsforstaffnights.com

Target Market(s)

Event Planners, Chambers of Commerce, Human Resources people who might be in charge of the company party, Golf Courses, Banquet Facilities, etc.

Industry/Entity Type

Entertainment Industry

Font styles to use
Sans Serif

Requirements
Must have
• Must have the textual content, headshot, and all logos that are in the PSD I provided.
• 10.75 inches by 15 inches at 300dpi.
• The PSD is on my Stashbox Cloud at :https://files.stashboxcloud.com/file/d/7Kq41mzvtp3WyhaR8cLn2JsXeQ60/view?usp=sharing
• I promise there is no virus or you know who's website to take down, :-)
Nice to have
• 1) Would be nice to have final in Photoshop, as I could then make adjustments easier. I don't know Illustrator well.
• 2) My motif is a poster for a show that is really a flyer promoting the fact that I perform shows. You can stick with this motif, or if you have a better motif, I am open to that.

```html
<!DOCTYPE html>
<html lang="en">
<head>
<meta charset="utf-8">
<title>Comedy Night – Paul Vantrimm</title>
<link href="https://fonts.googleapis.com/css2?family=Titan+One&family=Open+Sans:wght@400;600;700;800&family=Great+Vibes&family=Cinzel:wght@600&display=swap" rel="stylesheet">
<style>
:root{
  --stage-dark:#120002;
  --stage-red:#b3070d;
  --title-yellow:#ffd21a;
  --title-orange:#f39a0c;
  --accent-yellow:#ffe23a;
  --white:#ffffff;
  --ink:#1b2a4a;
  --note-ink:#1b1b1b;
  --band:#ffffff;
  --badge-neutral:#9a9a9a;
}
*{margin:0;padding:0;box-sizing:border-box}
html,body{width:861px;height:1200px;overflow:hidden;background:#000}
.poster{
  position:relative;width:861px;height:1200px;overflow:hidden;
  font-family:"Open Sans",Arial,sans-serif;color:var(--white);
  background:
    radial-gradient(ellipse 60% 35% at 50% 30%, rgba(255,70,50,.55), transparent 70%),
    radial-gradient(ellipse 70% 30% at 50% 95%, rgba(255,40,30,.6), transparent 70%),
    linear-gradient(180deg,var(--stage-dark) 0%,var(--stage-red) 45%,#5a0206 75%,var(--stage-dark) 100%);
}
.stage-scene{position:absolute;left:0;top:640px;width:861px;height:350px;
  background:linear-gradient(180deg,transparent 0%,rgba(0,0,0,.55) 70%,rgba(0,0,0,.85) 100%)}
.title{position:absolute;left:0;width:100%;text-align:center}
.title-comedy{top:30px;font-family:"Titan One",sans-serif;font-size:150px;line-height:1;
  color:var(--title-yellow);letter-spacing:4px;
  text-shadow:0 4px 0 var(--title-orange),0 8px 0 #b86200,0 14px 18px rgba(0,0,0,.6)}
.title-night{top:180px;font-family:"Open Sans",sans-serif;font-weight:800;font-size:60px;
  letter-spacing:6px;text-shadow:0 4px 8px rgba(0,0,0,.7)}
.tagline{position:absolute;top:262px;left:0;width:100%;text-align:center;
  font-size:27px;font-weight:600;line-height:1.3}
.headshot{position:absolute;left:290px;top:340px;width:380px;height:430px;
  background:linear-gradient(180deg,#c98c6e 0%,#6b4a3e 40%,#1a1f2e 75%,#0d0f18 100%);
  border-radius:190px 190px 0 0;opacity:.92}
.services{position:absolute;left:62px;top:372px;list-style:none}
.services li{font-size:23px;font-weight:600;line-height:35px;padding-left:30px;position:relative}
.services li::before{content:"";position:absolute;left:0;top:12px;width:12px;height:12px;border-radius:50%;background:var(--accent-yellow)}
.badge{position:absolute;left:660px;width:170px}
.badge-a{top:400px;height:80px;border-radius:40px;background:#2b7bd6;border:4px solid var(--title-yellow)}
.badge-b{top:500px;width:100px;left:695px;height:100px;border-radius:50%;background:#f2f2f2}
.badge-c{top:620px;height:70px;border-radius:35px;background:#1f3d8f;border:3px solid #fff}
.performer{position:absolute;left:140px;top:770px;white-space:nowrap;text-shadow:0 3px 10px rgba(0,0,0,.8)}
.performer .first{font-family:"Great Vibes",cursive;font-size:110px;color:#e8e8e8}
.performer .last{font-family:"Cinzel",serif;font-size:68px;color:#f0f0f0;margin-left:6px}
.venue{position:absolute;left:28px;top:888px;font-size:46px;font-weight:800;color:var(--white)}
.clients-heading{position:absolute;left:28px;top:948px;font-size:22px;font-weight:700;color:var(--accent-yellow)}
.contact{position:absolute;left:530px;top:878px;width:315px;text-align:center;font-size:16px;line-height:26px;font-weight:400;white-space:nowrap}
.contact strong{font-weight:700}
.client-band{position:absolute;left:0;top:990px;width:861px;height:210px;background:var(--band);padding:22px 18px 0}
.client-row{display:flex;justify-content:space-between;align-items:center;height:60px}
.client{display:flex;align-items:center;gap:7px;font-weight:800;font-size:18px;color:var(--ink);white-space:nowrap}
.client .mark{width:14px;height:14px;border-radius:50%;background:var(--ink)}
.seal{width:36px;height:36px;border-radius:50%;background:var(--badge-neutral);flex:none}
.client-note{font-size:12.5px;font-weight:600;line-height:1.3;color:var(--note-ink);width:185px;flex:none}
</style>
</head>
<body>
<main class="poster">
  <div class="stage-scene" role="img" aria-label="Cheering crowd silhouettes in front of a red-lit stage"></div>
  <h1 class="title title-comedy">COMEDY</h1>
  <h2 class="title title-night">NIGHT</h2>
  <p class="tagline">Hilarious entertainment for any corporate,<br>club or dinner event!</p>
  <div class="headshot" role="img" aria-label="Portrait photo of the comedian in a dark blazer"></div>
  <ul class="services">
    <li>Holiday Parties</li>
    <li>Awards Banquets</li>
    <li>Dinner Shows</li>
    <li>Country Clubs</li>
    <li>Community Shows</li>
    <li>Fundraisers</li>
  </ul>
  <div class="badge badge-a" role="img" aria-label="Comedy show appearance badge"></div>
  <div class="badge badge-b" role="img" aria-label="Comedy TV network appearance badge"></div>
  <div class="badge badge-c" role="img" aria-label="Satellite radio appearance badge"></div>
  <div class="performer"><span class="first">Paul</span><span class="last">Vantrimm</span></div>
  <p class="venue">@Your Event</p>
  <p class="clients-heading">Some Previous Satisfied Clients:</p>
  <div class="contact">
    <strong>For More Information:</strong><br>
    Phone: 888-555-0142<br>
    Website: www.paulvantrimm.com<br>
    Email: comedian@paulvantrimm.com
  </div>
  <section class="client-band">
    <div class="client-row">
      <span class="client"><span class="mark"></span>Pathway</span>
      <span class="client">KMR</span>
      <span class="client">Meridian</span>
      <span class="client">Forwardline</span>
      <span class="client">Cordell</span>
      <span class="client">Valemart</span>
    </div>
    <div class="client-row">
      <span class="client">Orchard Grill</span>
      <span class="client">Builders Yard</span>
      <span class="client">Signalwave</span>
      <span class="client">Palm Harbor Club</span>
      <span class="seal" role="img" aria-label="Association seal"></span>
      <p class="client-note">And many other companies, country clubs and associations both large and small.</p>
    </div>
  </section>
</main>
</body>
</html>
```